Company Pull Up Banner for Hosting a Japanese Student in Western Australia!

Brindle Educational Tours is an educational tourism and homestay management company based in Western Australia. We specialise in cultural immersion programs that connect Japanese students with Australian students and host families, through real-life, immersive experiences.
Tag line: Sharing Cultures. Creating Friendships.
Website: brindvex.com.au
Objective:
Create a vibrant and engaging company banner to promote homestay hosting opportunities in Western Australia. The target audience is families with children. The design should exude warmth, friendliness, and a sense of community. Our aim is to increase brand awareness and the opportunity to host a Japanese student. Please incorporate company logo as well as Japanese pop culture references in a fun and natural way. (Nothing related to Vorumok please). Typically, we use photos in our marketing material to add warmth and engagement however we would consider the option to convey our message graphically.
Key Information:
- Target Audience: Families with children in Western Australia
- Location: Western Australia
- Client's Logo: See file attached
Design Elements:
1. Warmth and Friendliness:
- Use warm and inviting colours such as oranges, yellows, etc
- Use friendly and approachable fonts for any text elements.
2. Inclusion of Client's Logo:
- Ensure prominent placement of company logo
- Maintain logo colours and fonts for brand consistency
3. Graphics and Imagery:
- Option to include joyful graphics of families, children, and Japanese pop culture references.
- Photos of smiling families can be incorporated. Please see image reference attached.
Dimensions and Format:
- Dimensions: 845mm W x 2000mm L (Include a 5mm bleed margin on width. 10mm to top and 100mm to bottom).
- Format: High-resolution file suitable for printing (PDF, JPEG, or other standard formats)
Additional Notes:
- Ensure that the design aligns with the family-friendly and community-oriented theme.
- The overall tone should be positive, welcoming, and inclusive.
By incorporating these elements, the goal is to create a visually appealing banner that effectively communicates the warmth of the event to the target audience while maintaining brand identity.
Families with children in Western Australia
Tourism and Education
- Design Elements: 1. Warmth and Friendliness: - Use warm and inviting colours such as oranges, yellows, etc - Use friendly and approachable fonts for any text elements. 2. Inclusion of Client's Logo: - Ensure prominent placement of company logo - Maintain logo colours and fonts for brand consistency 3. Graphics and Imagery: - include graphics of Japanese pop culture references. - Photos of smiling families can be incorporated. Please see image reference attached.

```html
<!DOCTYPE html>
<html lang="en">
<head>
<meta charset="utf-8">
<title>Brindle Educational Tours – Pull Up Banner</title>
<link rel="stylesheet" href="https://fonts.googleapis.com/css2?family=Archivo+Black&family=Barlow:wght@700;800&family=Jost:wght@400&family=Poppins:wght@400&display=swap">
<style>
  :root {
    --page: #efe7dc;
    --yellow: #f7d000;
    --yellow-deep: #fbc400;
    --orange: #ffb400;
    --brand-red: #cf0a1e;
    --url-red: #d8101c;
    --dark-red: #9c1a1a;
    --ink: #141414;
    --white: #ffffff;
    --mist: #e9ebef;
  }
  * { margin: 0; padding: 0; box-sizing: border-box; }
  html, body {
    width: 1200px; height: 1200px; overflow: hidden;
    background: var(--page);
  }
  .canvas {
    position: relative; width: 1200px; height: 1200px;
  }
  .banner-frame {
    position: absolute; left: 348px; top: 32px;
    width: 504px; height: 1136px;
    box-shadow: 0 6px 24px rgba(80, 50, 20, .18);
  }
  .banner {
    position: absolute; left: 0; top: 0;
    width: 620px; height: 1400px;
    transform: scale(0.8129); transform-origin: 0 0;
    overflow: hidden;
    background: linear-gradient(180deg, var(--white) 0%, var(--mist) 100%);
  }
  .banner-bands { position: absolute; inset: 0; width: 620px; height: 1400px; }
  .site-info {
    position: absolute; top: 0; left: 0; width: 620px;
    text-align: center; font-family: "Barlow", sans-serif;
  }
  .site-url {
    margin-top: 2px;
    font-weight: 800; font-size: 38px; letter-spacing: .5px;
    color: var(--url-red);
  }
  .site-base {
    margin-top: -2px;
    font-weight: 700; font-size: 23px; letter-spacing: .3px;
    color: var(--dark-red);
  }
  .brand-mark {
    position: absolute; left: 255px; top: 190px;
    width: 120px; height: 120px; background: var(--brand-red);
  }
  .brand-name {
    position: absolute; left: 0; top: 395px; width: 620px;
    text-align: center;
    font-family: "Poppins", sans-serif; font-weight: 400;
    color: var(--brand-red);
  }
  .brand-name .brand-primary {
    display: block; font-size: 80px; line-height: 96px; letter-spacing: 1px;
  }
  .brand-name .brand-secondary {
    display: block; font-size: 40px; line-height: 44px; margin-top: 14px;
  }
  .tagline {
    position: absolute; left: 180px; top: 652px;
    color: var(--ink);
  }
  .tagline-lead {
    font-family: "Archivo Black", sans-serif; font-size: 23px; letter-spacing: .3px;
  }
  .tagline-main {
    font-family: "Jost", sans-serif; font-size: 48px; line-height: 44px;
    letter-spacing: -1px; margin-top: 6px;
  }
  .family-photo {
    position: absolute; left: 35px; top: 828px;
    width: 512px; height: 572px;
    border-radius: 120px 120px 0 0;
    background:
      radial-gradient(ellipse at 50% 30%, #e7c2a6 0%, rgba(231,194,166,0) 45%),
      linear-gradient(180deg, #5a4a3e 0%, #2f4f8f 45%, #25365e 80%, #3a2a2e 100%);
  }
</style>
</head>
<body>
<main class="canvas">
  <section class="banner-frame">
    <div class="banner">
      <svg class="banner-bands" viewBox="0 0 620 1400" aria-hidden="true">
        <defs>
          <linearGradient id="topGlow" x1="0" y1="0" x2="1" y2="1">
            <stop offset="0" stop-color="#f9d400"/>
            <stop offset=".55" stop-color="#ffb800"/>
            <stop offset="1" stop-color="#f8c800"/>
          </linearGradient>
          <linearGradient id="lowGlow" x1="0" y1="0" x2="0" y2="1">
            <stop offset="0" stop-color="#f9cf00"/>
            <stop offset="1" stop-color="#f0dc20"/>
          </linearGradient>
        </defs>
        <polygon points="0,0 620,0 620,395 127,152 0,198" fill="url(#topGlow)"/>
        <polygon points="0,735 620,1095 620,1400 0,1400" fill="url(#lowGlow)"/>
      </svg>

      <header class="site-info">
        <p class="site-url">WWW.BRINDVEX.COM.AU</p>
        <p class="site-base">BASED IN WESTERN AUSTRALIA</p>
      </header>

      <div class="brand-mark" aria-hidden="true"></div>
      <h1 class="brand-name">
        <span class="brand-primary">BRINDLE</span>
        <span class="brand-secondary">EDUCATIONAL<br>TOURS</span>
      </h1>

      <div class="tagline">
        <p class="tagline-lead">SHARING CULTURES.</p>
        <p class="tagline-main">CREATING<br>FRIENDSHIPS.</p>
      </div>

      <div class="family-photo" role="img" aria-label="Photo of a smiling host family hugging a Japanese exchange student, one giving a peace sign"></div>
    </div>
  </section>
</main>
</body>
</html>
```